Harold Brisk Mechanical business cards

We need business cards designed for "Harold Brisk Mechanical" "Mechanical & Electrical Contractors" "Specializing in Service & Installation"
"Cooling, Heating, Service, Installations, Residential, Commercial"

```html
<!DOCTYPE html>
<html lang="en">
<head>
<meta charset="UTF-8">
<title>Harold Brisk Mechanical – Business Cards</title>
<link rel="stylesheet" href="https://fonts.googleapis.com/css2?family=Montserrat:wght@400;500;600;700&family=Lato:wght@400&display=swap">
<style>
  :root {
    --brand-red: #e8262d;
    --ink: #1b1b1b;
    --card-black: #1d1d1d;
    --paper: #ffffff;
    --backdrop: #d9d9d9;
    --muted: #2a2a2a;
  }
  * { box-sizing: border-box; margin: 0; padding: 0; }
  html, body { width: 1200px; height: 900px; overflow: hidden; }
  body {
    background: var(--backdrop);
    font-family: "Montserrat", sans-serif;
    position: relative;
  }
  .card {
    position: absolute;
    left: 290px;
    width: 620px;
    height: 354px;
    overflow: hidden;
    box-shadow: 0 6px 18px rgba(0,0,0,0.18);
  }
  .card--front { top: 80px; background: var(--paper); border-left: 5px solid var(--brand-red); border-bottom: 5px solid var(--brand-red); }
  .card--back { top: 466px; background: var(--card-black); }

  /* wordmark */
  .wordmark { display: flex; align-items: center; gap: 12px; }
  .wordmark__square { width: 34px; height: 34px; background: var(--brand-red); flex: none; }
  .wordmark__name {
    font-family: "Montserrat", sans-serif;
    font-weight: 600;
    text-transform: uppercase;
    line-height: 1.1;
  }

  /* front */
  .front__wordmark { position: absolute; top: 48px; right: 42px; }
  .front__wordmark .wordmark__name { color: var(--ink); font-size: 20px; letter-spacing: 0.5px; }
  .front__person { position: absolute; left: 40px; top: 150px; }
  .front__name { color: var(--brand-red); font-weight: 700; font-size: 32px; }
  .front__title { color: var(--muted); font-weight: 500; font-size: 16px; margin-top: 2px; }
  .front__rule { position: absolute; left: 40px; right: 40px; top: 232px; height: 1.5px; background: var(--brand-red); }
  .front__contacts { position: absolute; left: 40px; top: 250px; list-style: none; font-size: 15px; color: var(--muted); font-weight: 500; }
  .front__contacts li { display: flex; align-items: center; gap: 10px; height: 24px; }
  .front__contacts svg { width: 13px; height: 13px; fill: var(--brand-red); flex: none; }
  .front__web-domain { color: var(--brand-red); }
  .front__address { position: absolute; right: 42px; top: 254px; text-align: right; font-size: 15px; color: var(--muted); font-weight: 500; line-height: 1.55; font-style: normal; }

  /* back */
  .back__wordmark { position: absolute; top: 70px; left: 0; right: 0; justify-content: center; }
  .back__wordmark .wordmark__square { width: 46px; height: 46px; }
  .back__wordmark .wordmark__name { color: var(--paper); font-size: 34px; letter-spacing: 1px; }
  .back__tagline {
    position: absolute; top: 200px; left: 0; right: 0; text-align: center;
    font-family: "Lato", sans-serif; color: var(--paper); font-size: 19px; line-height: 1.35;
  }
  .back__band { position: absolute; left: 0; right: 0; bottom: 0; height: 7px; background: var(--brand-red); }
</style>
</head>
<body>

<section class="card card--front" aria-label="Business card front">
  <div class="wordmark front__wordmark">
    <span class="wordmark__square"></span>
    <span class="wordmark__name">Harold Brisk<br>Mechanical</span>
  </div>

  <div class="front__person">
    <h1 class="front__name">Daniel Okafor</h1>
    <p class="front__title">Managing Partner</p>
  </div>

  <div class="front__rule"></div>

  <ul class="front__contacts">
    <li>
      <svg viewBox="0 0 24 24" aria-hidden="true"><path d="M6.6 10.8a15.1 15.1 0 0 0 6.6 6.6l2.2-2.2a1 1 0 0 1 1-.25 11.4 11.4 0 0 0 3.6.57 1 1 0 0 1 1 1V20a1 1 0 0 1-1 1A17 17 0 0 1 3 4a1 1 0 0 1 1-1h3.5a1 1 0 0 1 1 1c0 1.25.2 2.45.57 3.57a1 1 0 0 1-.25 1z"/></svg>
      555-014-2290
    </li>
    <li>
      <svg viewBox="0 0 24 24" aria-hidden="true"><path d="M2 5h20v14H2zm2 2v.5l8 5 8-5V7l-8 5z"/></svg>
      info@haroldbrisk.com
    </li>
    <li>
      <svg viewBox="0 0 24 24" aria-hidden="true"><path d="M12 2a10 10 0 1 0 0 20 10 10 0 0 0 0-20zm0 2.2c1 1.2 1.8 3 2.1 4.8H9.9c.3-1.8 1.1-3.6 2.1-4.8zM4.6 11h3.2a15 15 0 0 0 0 2H4.6a7.6 7.6 0 0 1 0-2zm5.2 0h4.4a13 13 0 0 1 0 2H9.8a13 13 0 0 1 0-2zm6.4 0h3.2a7.6 7.6 0 0 1 0 2h-3.2a15 15 0 0 0 0-2zM12 19.8c-1-1.2-1.8-3-2.1-4.8h4.2c-.3 1.8-1.1 3.6-2.1 4.8z"/></svg>
      <span>www.<span class="front__web-domain">haroldbrisk</span>.com</span>
    </li>
  </ul>

  <address class="front__address">
    1187 Larkspur Lane<br>
    Fairhaven, TN 38000
  </address>
</section>

<section class="card card--back" aria-label="Business card back">
  <div class="wordmark back__wordmark">
    <span class="wordmark__square"></span>
    <span class="wordmark__name">Harold Brisk Mechanical</span>
  </div>

  <p class="back__tagline">
    Harold Brisk Mechanical<br>
    Mechanical &amp; Electrical Contractors - Specializing in Service &amp; Installation<br>
    Cooling - Heating - Service - Installations - Residential - Commercial
  </p>

  <div class="back__band"></div>
</section>

</body>
</html>
```